Business Card needed for Drainor, a growing Septic Service company

Drainor, a growing local septic service company in Pennsylvania, needs updated business cards. We'd like the business card to feature our logo and communicate that we provide Septic Pumping, Installations/Repairs, Restroom Rentals, and 24/7 Emergency Service. The business card should be eye-catching, bold, and clean/simple. We have been in business almost 10 years and would like to expand and update our business brand and image.

Target Market(s)

Residential and Commercial, New and Current Homeowners

Industry/Entity Type

Service

Contact Information for Business Card

Contact on the business card should be: Dean Harlow Owner & Operator
Phone: 610-555-0187
Email: service@drainor-example.com
Website: www.drainor-example.com
Address: 812 Millbrook Lane Easton PA 18042

Font styles to use
Sans Serif

Colors

Designer to choose colors to be used in the design.

Requirements
Must have
• Feature logo on both side of business card.
Nice to have
• We envision the contact information on one side and our services listed on the other side. Utilize the green from the symbol in our logo as part of the design, overall design color scheme should be white, grey, black.

```html
<!DOCTYPE html>
<html lang="en">
<head>
<meta charset="utf-8">
<title>Drainor — Business Card Front</title>
<link rel="stylesheet" href="https://fonts.googleapis.com/css2?family=Krona+One&display=swap">
<style>
  :root {
    --card-white: #ffffff;
    --ink-black: #111314;
    --brand-green: #80ff00;
    --pale-green: #eefad8;
    --deep-green: #4d7f1c;
    --slate-grey: #43484a;
    --charcoal: #262a2b;
  }
  html, body {
    margin: 0;
    padding: 0;
    width: 1200px;
    height: 686px;
    overflow: hidden;
    background: var(--card-white);
  }
  .card-front {
    position: relative;
    width: 1200px;
    height: 686px;
    overflow: hidden;
    background: var(--card-white);
  }
  .wave-backdrop {
    position: absolute;
    inset: 0;
    width: 1200px;
    height: 686px;
    display: block;
  }
  .brand-lockup {
    position: absolute;
    left: 311px;
    top: 295px;
    height: 100px;
    display: flex;
    align-items: center;
    gap: 26px;
  }
  .brand-square {
    width: 100px;
    height: 100px;
    background: var(--brand-green);
    flex: none;
  }
  .brand-name {
    font-family: "Krona One", sans-serif;
    font-size: 68px;
    line-height: 1;
    color: var(--ink-black);
    letter-spacing: 2px;
    margin: 0;
    font-weight: 400;
  }
</style>
</head>
<body>
  <main class="card-front">
    <svg class="wave-backdrop" viewBox="0 0 1200 686" aria-hidden="true">
      <path class="wave-pale" fill="var(--pale-green)"
        d="M0,514 C200,560 350,600 470,610 L800,606 C1000,560 1130,440 1200,300 L1200,686 L0,686 Z"/>
      <path class="wave-bright" fill="var(--brand-green)"
        d="M0,660 C200,590 380,560 500,572 C640,585 720,630 840,622 C960,615 1100,590 1200,566 L1200,686 L0,686 Z"/>
      <ellipse class="disc-slate" cx="-128" cy="610" rx="210" ry="260" fill="var(--slate-grey)"/>
      <circle class="disc-shade" cx="-30" cy="900" r="350" fill="var(--charcoal)" opacity="0.55"/>
      <path class="disc-green-overlap" fill="var(--deep-green)" opacity="0.85"
        d="M60,686 C120,650 170,625 230,605 C260,630 290,660 310,686 Z"/>
    </svg>

    <div class="brand-lockup">
      <span class="brand-square"></span>
      <h1 class="brand-name">DRAINOR</h1>
    </div>
  </main>
</body>
</html>
```